QEV Blaze Global Packaging for Retail sales sachets and boxes

Firstly what is QEV Blaze - QEV Blaze is a powerful combustion and cleaning technology, developed to help enhance engine performance and responsiveness. Its unique double action formulation is designed to actively clean your engine and protect vital engine parts to help deliver more powerful performance. http://qevtechnics.com.au/
We are branching out into retail sales and require dynamic and innovative packaging to suit an international market place in western and eastern markets.
The core image is the Singapore Lion and the flame, enhancing the visual impact of the flame inline with the QEV colour scheme is desired. QEV Blaze is the product name. For the boxes key info Patented Nitroparaffins, Improved Detergency & Combustion *U.S.EPA Registered* / *U.S. Patents*, Directions for Use: Fill fuel tank, tear sachet, pour contents of sachet into fuel tank, ideal mix ratio is 1ml QEV to every 1L of fuel, (diesel or petrol - depending on the targeted market), Circular flammable symbol with a line through the struck match, FLAMMABLE, Keep away from heat, sparks, and open flame. DO NOT puncture packageing, each box contains X sachets of X mls each, Distributed by: Distributed by: QEV Technics Australia, 47 Tembusu Lane, Singapore 077412, Packaged by: Rivora-Seal Works Sdn Bhd (736492-K) 7C Wisma Kelara Hadi, 9 Jalan Tepian, 10000 Penang, Malaysia Tel/Fax: +604-517 2946 Email: rsw@rivoraseal.net.my Website: http://www.rivoraseal.net.my., MSDS available on website
Sachets: There are two products QEV100 for petrol engines and QEV200 for diesel engines.
Info for sachets: QEV Blaze, the Lion image as per above, QEV100 (this will be either QEV100 or QEV 200), Additive for Petrol Engine (or diesel engines depending on content of sachet), Directions for Use, Fill fuel tank, tear sachet, pour contents of sachet into fuel tank, ideal mix ratio is 1ml QEV to every 1L of fuel, Net Content Xml, QEV is a patented fuel technology that uses a nitro paraffin concentrate, blended with fuels to improve their atomization, lubricity and combustion quality to achieve more green mileage (we will consider changing this wording if a better description is presented), Circular flammable symbol with a line through the struck match, FLAMMABLE, Keep away from heat, sparks, and open flame. DO NOT puncture packageing, Distributed by: QEV Technics Australia, 47 Tembusu Lane, Singapore 077412, info@qevtechnics.com.au. MSDS available on website, Please refer to the attached packaging size specifications, refer to the webpage etc to ensure uniformity of branding.
Updates

To all the designers thank you for your interest. After viewing some of the first submission I need to clarify that the images of the packaging sachets and boxes is just info please refer to the design brief for the required content. Look forward to your submissions

Project Deadline Extended
Reason: Finalist designs set to board for comment and additional time required to finalise the amendments required.

Industry/Entity Type

Retail

```html
<!DOCTYPE html>
<html lang="en">
<head>
<meta charset="utf-8">
<title>QEV Blaze – QEV 100 Sachet</title>
<link href="https://fonts.googleapis.com/css2?family=Exo+2:ital,wght@0,400;0,600;0,800;1,400&display=swap" rel="stylesheet">
<style>
  :root{
    --navy:#1f2a84;
    --navy-deep:#18216b;
    --sky:#1b9ad7;
    --panel:#e8e8ea;
    --paper:#ffffff;
    --ink:#1f2a84;
    --alert:#e2412b;
    --backdrop:#ffffff;
  }
  *{box-sizing:border-box;margin:0;padding:0}
  html,body{width:927px;height:1200px;overflow:hidden;background:var(--backdrop)}
  body{font-family:"Exo 2",sans-serif;position:relative}
  .sachet{
    position:absolute;left:133px;top:180px;width:660px;height:840px;
    background:var(--paper);border:1px solid var(--navy-deep);
    display:flex;flex-direction:column;overflow:hidden;
  }
  .edge-band{height:42px;background:var(--navy);flex:none}
  .edge-band.bottom{height:48px;margin-top:auto}
  .brand-panel{
    height:150px;background:linear-gradient(180deg,var(--panel),var(--paper) 60%,var(--panel));
    display:flex;align-items:center;gap:16px;padding-left:48px;flex:none;
  }
  .brand-dot{width:44px;height:44px;border-radius:50%;background:var(--sky);flex:none}
  .brand-name{font-weight:600;font-size:48px;color:var(--sky);letter-spacing:.5px}
  .product-band{
    background:var(--navy);color:#fff;height:210px;flex:none;
    display:flex;flex-direction:column;align-items:center;justify-content:center;
  }
  .product-code{font-weight:800;font-size:118px;line-height:1;letter-spacing:2px}
  .product-type{font-weight:600;font-size:36px;margin-top:6px}
  .info{padding:26px 44px 0;color:var(--ink);flex:1;display:flex;flex-direction:column}
  .directions-title{font-weight:600;font-size:24px}
  .directions{font-size:22px;line-height:1.22;margin-bottom:16px}
  .about{font-size:17px;line-height:1.25}
  .info-foot{display:flex;justify-content:space-between;align-items:flex-start;margin-top:22px;gap:20px}
  .warning{display:flex;gap:10px;align-items:flex-start;color:var(--alert);width:280px}
  .warning svg{flex:none}
  .warning-title{font-weight:600;font-size:19px}
  .warning-text{font-size:14px;line-height:1.2}
  .distributor{font-size:13.5px;line-height:1.3;color:var(--ink);width:260px;padding-top:30px}
  .distributor strong{font-weight:600}
</style>
</head>
<body>
  <main class="sachet">
    <div class="edge-band"></div>
    <header class="brand-panel">
      <span class="brand-dot" aria-hidden="true"></span>
      <span class="brand-name">QEV Blaze</span>
    </header>
    <section class="product-band">
      <h1 class="product-code">QEV 100</h1>
      <p class="product-type">Additive for petrol engine</p>
    </section>
    <section class="info">
      <h2 class="directions-title">Directions for Use:</h2>
      <p class="directions">Fill fuel tank, tear sachet, pour contents of sachet into fuel tank, ideal mix ratio is 1ml QEV to every 1L of fuel, Net Content Xml.</p>
      <p class="about">QEV is a patented fuel technology that uses a nitro paraffin concentrate, blended with fuels to improve their atomization, lubricity and combustion quality to achieve more green mileage</p>
      <div class="info-foot">
        <div class="warning">
          <svg width="44" height="44" viewBox="0 0 44 44" aria-hidden="true">
            <circle cx="22" cy="22" r="20" fill="var(--alert)"/>
            <circle cx="22" cy="22" r="16" fill="none" stroke="#fff" stroke-width="2"/>
            <path d="M22 9c2 5 8 8 8 15a8 8 0 0 1-16 0c0-4 2-6 4-8 0 3 1 5 3 5-1-4 0-8 1-12z" fill="#fff"/>
          </svg>
          <div>
            <p class="warning-title">FLAMMABLE</p>
            <p class="warning-text">Keep away from heat, sparks, and open flame. DO NOT puncture packageing.</p>
          </div>
        </div>
        <p class="distributor"><strong>Distributed by:</strong> QEV Technics Australia, 47 Tembusu Lane, Singapore 077412, info@qevtechnics.com.au.</p>
      </div>
    </section>
    <div class="edge-band bottom"></div>
  </main>
</body>
</html>
```